Business Consulting Company needs a business card designed

We need a business card in Brisbane Australia for a company called " Marrowvale Consulting Group". I would like to see the designs either in purple or green color

```html
<!DOCTYPE html>
<html lang="en">
<head>
<meta charset="utf-8">
<title>Marrowvale Consulting Group – Business Card</title>
<link rel="stylesheet" href="https://fonts.googleapis.com/css2?family=Bellefair&family=Open+Sans:wght@400;600&display=swap">
<style>
  :root {
    --backdrop: #e9e7ea;
    --card: #ffffff;
    --purple: #6b2a7c;
    --green: #6cc04a;
    --on-purple: #ffffff;
    --divider: rgba(255,255,255,0.55);
  }
  * { margin: 0; padding: 0; box-sizing: border-box; }
  html, body {
    width: 1200px; height: 800px; overflow: hidden;
    background: var(--backdrop);
  }
  .card {
    position: absolute; left: 100px; top: 100px;
    width: 1000px; height: 600px;
    background: var(--card);
    overflow: hidden;
    box-shadow: 0 10px 30px rgba(0,0,0,0.18);
  }
  .card__swoosh { position: absolute; inset: 0; width: 1000px; height: 600px; }
  .brand {
    position: absolute; left: 60px; top: 165px;
    display: flex; align-items: center; gap: 20px;
  }
  .brand__dot {
    width: 60px; height: 60px; border-radius: 50%;
    background: var(--purple);
  }
  .brand__name {
    font-family: "Bellefair", serif;
    font-size: 48px; color: var(--purple);
    letter-spacing: 0.5px; white-space: nowrap;
  }
  .person {
    position: absolute; right: 400px; top: 522px;
    text-align: right;
  }
  .person__name {
    font-family: "Open Sans", sans-serif; font-weight: 600;
    font-size: 28px; color: var(--green); line-height: 1.1;
  }
  .person__role {
    font-family: "Open Sans", sans-serif;
    font-size: 18px; color: var(--on-purple);
  }
  .divider {
    position: absolute; left: 620px; top: 465px;
    width: 1.5px; height: 115px; background: var(--divider);
  }
  .contact {
    position: absolute; left: 640px; top: 443px;
    list-style: none;
    font-family: "Open Sans", sans-serif;
    font-size: 18px; color: var(--on-purple); line-height: 1.42;
  }
  .contact__item { display: flex; align-items: flex-start; gap: 9px; }
  .contact__icon { width: 18px; height: 18px; margin-top: 4px; flex: none; }
</style>
</head>
<body>
  <div class="card">
    <svg class="card__swoosh" viewBox="0 0 1000 600" aria-hidden="true">
      <path d="M560 418 C760 330 900 200 968 0 L1000 0 L1000 45 C900 225 760 340 560 418 Z" fill="var(--green)"/>
      <path d="M120 600 C420 540 750 400 1000 120 L1000 600 Z" fill="var(--purple)"/>
    </svg>

    <div class="brand">
      <span class="brand__dot"></span>
      <span class="brand__name">Marrowvale Consulting Group</span>
    </div>

    <div class="person">
      <p class="person__name">Elin Harrow</p>
      <p class="person__role">manager</p>
    </div>

    <span class="divider"></span>

    <ul class="contact">
      <li class="contact__item">
        <svg class="contact__icon" viewBox="0 0 20 20"><path d="M5 2l3 4-2 2c1 2 3 4 5 5l2-2 4 3-2 3C9 17 3 11 2 5z" fill="var(--green)"/></svg>
        <span>154-555-0182</span>
      </li>
      <li class="contact__item">
        <svg class="contact__icon" viewBox="0 0 20 20"><circle cx="10" cy="10" r="8" fill="none" stroke="var(--green)" stroke-width="2"/><path d="M2 10h16M10 2c-4 4-4 12 0 16M10 2c4 4 4 12 0 16" fill="none" stroke="var(--green)" stroke-width="1.5"/></svg>
        <span>www.marrowvaleconsult.com</span>
      </li>
      <li class="contact__item">
        <svg class="contact__icon" viewBox="0 0 20 20"><rect x="2" y="4" width="16" height="12" rx="1" fill="var(--green)"/><path d="M2 5l8 6 8-6" fill="none" stroke="var(--purple)" stroke-width="1.5"/></svg>
        <span>info@marrowvaleconsult.com</span>
      </li>
      <li class="contact__item">
        <svg class="contact__icon" viewBox="0 0 20 20"><path d="M10 2l8 7h-2v8h-4v-5H8v5H4V9H2z" fill="var(--green)"/></svg>
        <span>27 Fenwick Lane, Harlow Bay,<br>QLD 4102</span>
      </li>
    </ul>
  </div>
</body>
</html>
```